Website for new crypto research organization

See brief (attached). This is a pretty basic website with only a handful of pages + ability to collect email addresses.

```html
<!DOCTYPE html>
<html lang="en">
<head>
<meta charset="utf-8">
<title>Tealwave Digital</title>
<link rel="stylesheet" href="https://fonts.googleapis.com/css2?family=Archivo:wght@400;500;600;700;800&family=Space+Grotesk:wght@400;500;600&display=swap">
<style>
:root{
  --teal:#1a9a9c;
  --teal-dark:#168a8c;
  --blue:#1f8fc9;
  --ink:#1d1d1f;
  --body:#3a3a3c;
  --pale:#e3f4f5;
  --footer:#eaf6f8;
  --white:#ffffff;
  --line:#cfe3e6;
}
*{margin:0;padding:0;box-sizing:border-box}
html,body{width:1200px;height:3163px;overflow:hidden}
body{position:relative;background:var(--white);font-family:"Space Grotesk",sans-serif;color:var(--body)}
.abs{position:absolute}
h1,h2,h3,.heading{font-family:"Archivo",sans-serif;color:var(--ink);font-weight:800}

/* header */
.topline{left:0;top:0;width:1200px;height:4px;background:var(--teal)}
.brand{left:112px;top:18px;width:132px;height:72px;display:flex;flex-direction:column;justify-content:center;align-items:center;font-family:"Archivo",sans-serif;font-weight:700;color:var(--teal);font-size:19px;line-height:1.1;text-align:center}
.brand small{font-size:12px;letter-spacing:4px;font-weight:700}
.nav{top:44px;left:0;width:1200px;height:20px}
.nav a{position:absolute;font-family:"Archivo",sans-serif;font-weight:600;font-size:15px;color:var(--ink);text-decoration:none;letter-spacing:.2px}
.nav a.active{color:var(--teal)}
.nav a.active::after{content:"";position:absolute;left:0;right:0;top:25px;height:3px;background:var(--teal)}
.social-top{top:33px;width:42px;height:42px;border-radius:50%}
.social-top.filled{background:var(--teal)}
.social-top.ring{border:2px solid var(--teal)}

/* hero */
.hero{left:0;top:102px;width:1200px;height:600px;background:
 linear-gradient(90deg,rgba(0,0,0,0) 45%,rgba(0,0,0,0) 100%),
 linear-gradient(100deg,#9c9c98 0%,#b6b5b0 35%,#c9a84a 52%,#e06a7c 62%,#6fb0c2 76%,#c94e5c 90%,#a5a5a2 100%)}
.hero-floor{left:0;top:598px;width:1200px;height:104px;background:linear-gradient(180deg,#8e8b86,#b2aea8)}
.hero-frame{left:117px;top:264px;width:491px;height:276px;border:5px solid var(--teal);border-right-color:var(--blue);border-bottom-color:var(--blue)}
.hero-title{left:157px;top:303px;font-size:36px;letter-spacing:.3px}
.hero-sub{left:157px;top:360px;width:420px;font-family:"Archivo",sans-serif;font-weight:500;font-size:19px;line-height:28px;color:var(--ink)}
.btn-fill{left:157px;top:442px;width:145px;height:50px;background:linear-gradient(90deg,var(--teal),var(--blue));color:var(--white);font-family:"Archivo",sans-serif;font-weight:700;font-size:15px;display:flex;align-items:center;justify-content:center}
.slider-line{left:1142px;top:307px;width:2px;height:92px;background:var(--white)}
.slider-dot{left:1136px;width:14px;height:14px;border:2px solid var(--white);border-radius:50%}
.hero-badge{left:543px;top:645px;width:114px;height:114px;border-radius:50%;background:var(--white);border:1px solid #ddd}
.hero-badge-inner{left:562px;top:664px;width:76px;height:76px;border-radius:50%;background:var(--white);box-shadow:0 3px 10px rgba(0,0,0,.2)}

/* sections */
.sec-title{left:0;width:1200px;text-align:center;font-size:30px;letter-spacing:.3px}
.sec-rule{height:2px;background:linear-gradient(90deg,rgba(26,154,156,0),var(--teal),rgba(26,154,156,0))}
.card{top:939px;width:307px;height:332px;border:2px solid var(--teal);border-radius:4px;background:var(--white);text-align:center}
.card .icon{position:absolute;left:101px;top:34px;width:104px;height:104px;border-radius:50%;background:#bfe7ea}
.card .icon span{position:absolute;left:8px;top:8px;width:88px;height:88px;border-radius:50%;background:linear-gradient(135deg,var(--teal),var(--blue));display:flex;align-items:center;justify-content:center}
.card h3{position:absolute;left:0;width:100%;top:166px;font-size:20px}
.card p{position:absolute;left:14px;right:14px;top:202px;font-size:14.5px;line-height:26px}

/* about */
.about-band{left:0;top:1367px;width:1200px;height:470px;background:var(--pale)}
.about-art{left:0;top:1367px;width:577px;height:470px;background:linear-gradient(90deg,#5c4a3c 0%,#3f6f70 35%,#8a5a3e 60%,rgba(227,244,245,0) 100%)}
.about-frame{left:982px;top:1437px;width:101px;height:313px;border:7px solid #7fcfcf;border-left:none}
.about-frame-bottom{left:744px;top:1743px;width:245px;height:7px;background:#7fcfcf}
.about-title{left:599px;top:1428px;font-size:25px}
.about-text{left:599px;width:445px;font-size:14.5px;line-height:26px;text-align:justify}
.btn-line{border:2px solid var(--teal);font-family:"Archivo",sans-serif;font-weight:700;color:var(--ink);display:flex;align-items:center;justify-content:center;font-size:15px}

/* news */
.news{top:2036px;width:479px;height:303px;border-radius:4px;padding:28px 24px}
.news.light{background:var(--white);box-shadow:0 2px 10px rgba(0,0,0,.12)}
.news.dark{background:linear-gradient(135deg,var(--teal),var(--blue));color:var(--white)}
.news .date{font-size:16px;display:flex;align-items:center;gap:12px}
.tags{margin-top:20px;display:flex;flex-wrap:wrap;gap:8px 10px;width:420px}
.tag{height:44px;padding:0 15px;border:2px solid var(--teal);display:flex;align-items:center;font-family:"Archivo",sans-serif;font-weight:500;font-size:14px;color:var(--ink)}
.dark .tag{border-color:var(--white);color:var(--white)}
.news h4{margin-top:20px;font-family:"Space Grotesk",sans-serif;font-weight:500;font-size:20px;line-height:28px;color:var(--ink)}
.dark h4{color:var(--white)}
.news .more{margin-top:14px;font-family:"Archivo",sans-serif;font-weight:600;font-size:15px;color:var(--teal)}
.dark .more{color:var(--white)}

/* subscribe */
.sub{left:0;top:2522px;width:1200px;height:337px;background:linear-gradient(100deg,#1a9a9c 0%,#1d86b8 60%,#1e6fb0 100%)}
.sub-title{left:0;top:2582px;width:1200px;text-align:center;font-size:25px;color:var(--white)}
.sub-text{left:190px;top:2658px;width:820px;text-align:center;color:var(--white);font-size:15.5px;line-height:27px}
.field{top:2741px;height:51px;border:2px solid var(--white);color:var(--white);font-size:17px;display:flex;align-items:center;padding-left:15px}
.sub-btn{left:786px;top:2741px;width:145px;height:51px;background:var(--white);color:var(--blue);font-size:17px;display:flex;align-items:center;justify-content:center}

/* footer */
.footer{left:0;top:2859px;width:1200px;height:304px;background:var(--footer)}
.foot-brand{left:112px;top:2912px;width:216px;height:120px;display:flex;flex-direction:column;justify-content:center;align-items:center;font-family:"Archivo",sans-serif;font-weight:700;color:var(--teal);font-size:29px;line-height:1.15}
.foot-brand small{font-size:17px;letter-spacing:7px;font-weight:700}
.foot-head{top:2906px;font-family:"Archivo",sans-serif;font-weight:600;font-size:19px;color:var(--blue)}
.foot-list{top:2950px;list-style:none;font-size:15px;color:var(--body)}
.foot-list li{height:27.7px;display:flex;align-items:center;gap:16px}
.foot-list li::before{content:"»";color:var(--teal);font-size:14px}
.foot-social{left:963px;width:42px;height:42px;border-radius:50%;background:linear-gradient(135deg,var(--teal),var(--blue))}
.foot-social-label{left:1031px;font-size:15px}
.foot-rule{left:112px;top:3107px;width:976px;height:1px;background:var(--line)}
.copy{left:0;top:3128px;width:1200px;text-align:center;font-size:14px}
</style>
</head>
<body>

<header>
  <div class="abs topline"></div>
  <div class="abs brand">TEALWAVE<small>DIGITAL</small></div>
  <nav class="abs nav">
    <a class="active" style="left:377px" href="#">HOME</a>
    <a style="left:455px" href="#">ABOUT</a>
    <a style="left:541px" href="#">RESEARCH</a>
    <a style="left:656px" href="#">NEWS</a>
    <a style="left:734px" href="#">CAREERS</a>
    <a style="left:837px" href="#">CONTACT</a>
  </nav>
  <div class="abs social-top filled" style="left:1003px" aria-label="Chirpline"></div>
  <div class="abs social-top ring" style="left:1047px" aria-label="Worknet"></div>
</header>

<section>
  <div class="abs hero" role="img" aria-label="Concrete wall with a colourful geometric mural"></div>
  <div class="abs hero-floor" role="img" aria-label="Concrete floor"></div>
  <div class="abs hero-frame"></div>
  <h1 class="abs hero-title">TEALWAVE DIGITAL</h1>
  <p class="abs hero-sub">A thematic, research-driven digital asset investment firm built for founders</p>
  <div class="abs btn-fill">GET STARTED</div>
  <div class="abs slider-line"></div>
  <div class="abs slider-dot" style="top:418px"></div>
  <div class="abs slider-dot" style="top:441px"></div>
  <div class="abs slider-dot" style="top:464px"></div>
  <div class="abs slider-dot" style="top:487px"></div>
  <div class="abs hero-badge"></div>
  <div class="abs hero-badge-inner"></div>
</section>

<section>
  <h2 class="abs sec-title" style="top:826px">OUR RESEARCH PROCESS</h2>
  <div class="abs sec-rule" style="left:490px;top:876px;width:220px"></div>

  <div class="abs card" style="left:112px">
    <div class="icon"><span>
      <svg width="44" height="44" viewBox="0 0 44 44" fill="none" stroke="#fff" stroke-width="2"><rect x="5" y="7" width="28" height="22" rx="2"/><circle cx="26" cy="26" r="8"/><line x1="32" y1="32" x2="39" y2="39"/><line x1="10" y1="13" x2="22" y2="13"/></svg>
    </span></div>
    <h3>WHO WE ARE</h3>
    <p>Sed ut perspiciatis unde omnis iste nat us error sit voluptatem accusantium doloremque laudantium, totam rem aperiam, eaque ipsa.</p>
  </div>
  <div class="abs card" style="left:446px">
    <div class="icon"><span>
      <svg width="44" height="44" viewBox="0 0 44 44" fill="none" stroke="#fff" stroke-width="2"><path d="M4 22 Q22 6 40 22 Q22 38 4 22Z"/><circle cx="22" cy="22" r="7"/><circle cx="22" cy="22" r="2.5" fill="#fff"/></svg>
    </span></div>
    <h3>VISION</h3>
    <p>Sed ut perspiciatis unde omnis iste nat us error sit voluptatem accusantium doloremque laudantium, totam rem aperiam, eaque ipsa.</p>
  </div>
  <div class="abs card" style="left:780px">
    <div class="icon"><span>
      <svg width="44" height="44" viewBox="0 0 44 44" fill="none" stroke="#fff" stroke-width="2"><rect x="8" y="7" width="24" height="31" rx="2"/><rect x="15" y="4" width="10" height="6" rx="1"/><circle cx="27" cy="26" r="7"/><circle cx="27" cy="26" r="2"/><line x1="13" y1="17" x2="21" y2="17"/><line x1="13" y1="23" x2="18" y2="23"/></svg>
    </span></div>
    <h3>MISSION</h3>
    <p>Sed ut perspiciatis unde omnis iste nat us error sit voluptatem accusantium doloremque laudantium, totam rem aperiam, eaque ipsa.</p>
  </div>
</section>

<section>
  <div class="abs about-band"></div>
  <div class="abs about-art" role="img" aria-label="Painted city street scene in rust and teal tones"></div>
  <div class="abs about-frame"></div>
  <div class="abs about-frame-bottom"></div>
  <h2 class="abs about-title">ABOUT TEALWAVE DIGITAL</h2>
  <p class="abs about-text" style="top:1487px">Lorem ipsum dolor sit amet, consectetur adipiscing elit, sed do eiusm od tempor incididunt ut labore et dolore magna aliqua. Ut enim ad minim veniam, quis nostrud exercitation ullamco laboris nisi ut aliquip ex ea commodo consequat.</p>
  <p class="abs about-text" style="top:1603px">Duis aute irure dolor in reprehenderit in voluptate velit esse cillum dolore eu fugiat nulla pariatur. Excepteur sint occaecat cupidatat non proident in culpa qui officia deserunt.</p>
  <div class="abs btn-line" style="left:599px;top:1722px;width:146px;height:51px">LEARN MORE</div>
</section>

<section>
  <h2 class="abs sec-title" style="top:1926px;font-size:34px">LATEST NEWS</h2>
  <div class="abs sec-rule" style="left:560px;top:1980px;width:80px"></div>

  <article class="abs news light" style="left:112px">
    <div class="date"><svg width="14" height="14" viewBox="0 0 14 14" fill="#1a9a9c"><rect x="0" y="2" width="14" height="12" rx="1"/><rect x="2" y="5" width="10" height="7" fill="#fff"/></svg>09 Feb 2022</div>
    <div class="tags"><span class="tag">VALUATION</span><span class="tag">RESEARCH</span><span class="tag">TOKEN</span><span class="tag">REVIEW</span><span class="tag">ECONOMICS</span><span class="tag">THESES</span></div>
    <h4>At vero eos et accusamus et iusto odio dignis simos ducimus qui blanditiisea.</h4>
    <div class="more">Read More &nbsp;»</div>
  </article>
  <article class="abs news dark" style="left:609px">
    <div class="date"><svg width="14" height="14" viewBox="0 0 14 14" fill="#fff"><rect x="0" y="2" width="14" height="12" rx="1"/><rect x="2" y="5" width="10" height="7" fill="#1a9a9c"/></svg>09 Feb 2022</div>
    <div class="tags"><span class="tag">VALUATION</span><span class="tag">RESEARCH</span><span class="tag">TOKEN</span><span class="tag">REVIEW</span><span class="tag">ECONOMICS</span><span class="tag">THESES</span></div>
    <h4>At vero eos et accusamus et iusto odio dignis simos ducimus qui blanditiisea.</h4>
    <div class="more">Read More &nbsp;»</div>
  </article>

  <div class="abs btn-line" style="left:476px;top:2393px;width:247px;height:51px;font-size:14px">RECENT RESEARCH REPORTS</div>
</section>

<section>
  <div class="abs sub"></div>
  <h2 class="abs sub-title">SUBSCRIBE TO TEALWAVE DIGITAL</h2>
  <div class="abs sec-rule" style="left:495px;top:2632px;width:210px;background:linear-gradient(90deg,rgba(255,255,255,0),rgba(255,255,255,.6),rgba(255,255,255,0))"></div>
  <p class="abs sub-text">Sed ut perspiciatis unde omnis iste natus error sit voluptatem accusantium doloremque laudantium, totam rem architecto beatae vitae dicta sunt explicabo.</p>
  <div class="abs field" style="left:269px;width:246px">Name</div>
  <div class="abs field" style="left:528px;width:246px">Email</div>
  <div class="abs sub-btn">Subscribe</div>
</section>

<footer>
  <div class="abs footer"></div>
  <div class="abs foot-brand">TEALWAVE<small>DIGITAL</small></div>
  <div class="abs foot-head" style="left:445px">COMPANY</div>
  <ul class="abs foot-list" style="left:445px"><li>Home</li><li>About</li><li>Research</li><li>Careers</li><li>Contact</li></ul>
  <div class="abs foot-head" style="left:684px">OTHER LINKS</div>
  <ul class="abs foot-list" style="left:684px"><li>News</li><li>Disclaimer</li><li>Privacy Policy</li><li>Terms Of Use</li></ul>
  <div class="abs foot-head" style="left:963px">FOLLOW US</div>
  <div class="abs foot-social" style="top:2956px"></div>
  <div class="abs foot-social-label" style="top:2967px">Chirpline</div>
  <div class="abs foot-social" style="top:3005px"></div>
  <div class="abs foot-social-label" style="top:3016px">Worknet</div>
  <div class="abs foot-rule"></div>
  <p class="abs copy">© 2022 Tealwave Digital &nbsp;| &nbsp;All Rights Reserved</p>
</footer>

</body>
</html>
```